High Tech Software Startup needs Letterhead Design

We need a letterhead for a startup company base in Brazil. The letterhead should combine with our logo attached here.
We are a team of professionals in Java for web and mobile with iOS and android development.
We are looking for a modern and futuristc design.

Target Market(s)

CIO, IT managers of mid to big size companies

Industry/Entity Type

It Company

```html
<!DOCTYPE html>
<html lang="en">
<head>
<meta charset="utf-8">
<title>VELTRA Letterhead</title>
<link rel="stylesheet" href="https://fonts.googleapis.com/css2?family=Open+Sans:wght@300;400;600;700&display=swap">
<style>
  :root {
    --bg: #e9e7e4;
    --paper: #ffffff;
    --ink: #3a3d44;
    --ink-soft: #6b6e75;
    --navy: #1d3f7c;
    --blue: #1aa3dc;
    --rule: #2b2e35;
    --footer-start: #1ba6de;
    --footer-end: #1f3a78;
  }
  * { box-sizing: border-box; margin: 0; padding: 0; }
  html, body {
    width: 1200px;
    height: 1024px;
    overflow: hidden;
    background: var(--bg);
    font-family: "Open Sans", Arial, sans-serif;
    color: var(--ink);
  }
  .letterhead {
    position: absolute;
    left: 260px;
    top: 31px;
    width: 680px;
    height: 962px;
    background: var(--paper);
    box-shadow: 0 6px 24px rgba(0,0,0,0.12);
    overflow: hidden;
  }
  .brand {
    position: absolute;
    left: 56px;
    top: 48px;
    display: flex;
    align-items: center;
    gap: 12px;
  }
  .brand-mark {
    width: 30px;
    height: 30px;
    background: var(--blue);
  }
  .brand-name {
    font-weight: 700;
    font-size: 40px;
    letter-spacing: 1px;
    color: var(--navy);
    line-height: 1;
  }
  .divider {
    position: absolute;
    left: 470px;
    top: 96px;
    width: 1px;
    height: 44px;
    background: var(--rule);
  }
  .contacts {
    position: absolute;
    left: 490px;
    top: 98px;
    list-style: none;
    font-size: 10.5px;
    line-height: 15px;
    color: var(--ink-soft);
  }
  .contacts li { display: flex; align-items: center; gap: 6px; }
  .contacts svg { width: 9px; height: 9px; fill: var(--blue); flex: none; }
  .salutation {
    position: absolute;
    left: 56px;
    top: 118px;
    font-size: 14px;
    font-weight: 600;
  }
  .letter {
    position: absolute;
    left: 56px;
    top: 166px;
    width: 568px;
    font-size: 11.5px;
    line-height: 17px;
    color: var(--ink);
  }
  .letter p { margin-bottom: 14px; }
  .signature { margin-top: 22px; }
  .signature-name {
    font-size: 22px;
    font-weight: 300;
    color: var(--ink);
    line-height: 1.1;
  }
  .signature-role {
    font-size: 11px;
    color: var(--ink-soft);
  }
  .footer-band {
    position: absolute;
    left: 0;
    bottom: 0;
    width: 100%;
    height: 54px;
    background: linear-gradient(90deg, var(--footer-start), var(--footer-end));
    display: flex;
    align-items: center;
    padding-left: 120px;
    color: #ffffff;
    font-size: 12.5px;
    letter-spacing: 0.2px;
  }
</style>
</head>
<body>
  <main class="letterhead">
    <header class="brand">
      <span class="brand-mark"></span>
      <span class="brand-name">VELTRA</span>
    </header>

    <span class="divider"></span>

    <ul class="contacts">
      <li>
        <svg viewBox="0 0 10 10"><path d="M2 0.5l2 2-1 1.2c.6 1.3 1.7 2.4 3 3l1.2-1 2 2-1.3 1.8C4.6 9.3 0.7 5.4 0.2 2z"/></svg>
        1.000.200.3000
      </li>
      <li>
        <svg viewBox="0 0 10 10"><path d="M2 0.5l2 2-1 1.2c.6 1.3 1.7 2.4 3 3l1.2-1 2 2-1.3 1.8C4.6 9.3 0.7 5.4 0.2 2z"/></svg>
        1.000.200.3000
      </li>
      <li>
        <svg viewBox="0 0 10 10"><path d="M0 2h10v6H0z M0 2l5 3.5L10 2" stroke="#fff" stroke-width=".8"/></svg>
        name@yourname.com
      </li>
      <li>
        <svg viewBox="0 0 10 10"><circle cx="5" cy="5" r="4.5"/></svg>
        www.yourname.com
      </li>
    </ul>

    <h2 class="salutation">Lorem Ipsum,</h2>

    <section class="letter">
      <p>We build secure software platforms for web and mobile teams, with native apps for phones and tablets that scale with your business. Our engineers work closely with IT leaders to plan, design and deliver on time.</p>
      <p>From first workshop to final release, each project follows a clear roadmap with regular reviews, open reports and tested code. We keep systems fast, stable and easy to maintain.</p>
      <p>Our support desk stays available after launch, so updates, fixes and new features arrive without delay. We value long partnerships built on trust and results.</p>
      <p>Thank you for your interest. We look forward to discussing how our team can help your company grow.</p>
      <div class="signature">
        <div class="signature-name">Your Name</div>
        <div class="signature-role">Company Director</div>
      </div>
    </section>

    <footer class="footer-band">
      Your Address goes here Str name, City, Zip Code, Country Name
    </footer>
  </main>
</body>
</html>
```